Product Insert / Thank You

I'm looking for a small card to be designed that will be included with our product when it ships. It will be 2 sided with 1 side being a "thank you" with our logo and the other side containing the following text:We would love to hear your feedback! For every review we receive on our products, we donate 100% of the proceeds of your order to TIDEWELL -- a non profit organization dedicated to preserving our oceans!If you are not 100% satisfied with your purchase or have any problems, we will always resolve your issue. please contact us via Brisko if you need assistance.Insert needs to be well organized and information presented in a clear and visually appealing way.
Target Market(s)
Women, aged 24-45
Colors
Designer to choose colors to be used in the design.
Look and feel
Each slider illustrates characteristics of the customer's brand and the style your logo design should communicate.

```html
<!DOCTYPE html>
<html lang="en">
<head>
<meta charset="utf-8">
<title>Ridgeway Thank You Insert</title>
<link rel="stylesheet" href="https://fonts.googleapis.com/css2?family=Montserrat:wght@300;400;600;700;900&display=swap">
<style>
  :root {
    --page: #ffffff;
    --front-pink: #f08a9a;
    --back-pink: #f3a0ae;
    --panel-pink: #ef8499;
    --panel-pink-light: #f49aab;
    --white: #ffffff;
    --deep-rose: #b0405a;
    --plum: #5a2233;
    --faint-mark: #c96576;
    --gold: #c9b25a;
    --blossom-light: #fbe1e7;
    --blossom-mid: #f6c2cd;
    --ink: #111111;
    --shadow-line: #e0667e;
  }
  html, body {
    margin: 0;
    padding: 0;
    width: 1200px;
    height: 1200px;
    overflow: hidden;
    background: var(--page);
  }
  .insert-sheet {
    display: block;
    width: 1200px;
    height: 1200px;
    font-family: 'Montserrat', sans-serif;
  }
  .card-front { fill: var(--front-pink); }
  .card-back { fill: var(--back-pink); }
  .headline {
    font-family: 'Montserrat', sans-serif;
    font-weight: 900;
    fill: var(--white);
    letter-spacing: -2px;
  }
  .headline-rule { stroke: var(--shadow-line); stroke-width: 3; stroke-linecap: round; }
  .faint-mark-ring { fill: none; stroke: var(--faint-mark); stroke-width: 6; }
  .faint-mark-name {
    font-family: 'Montserrat', sans-serif;
    font-weight: 700;
    fill: var(--faint-mark);
    font-size: 44px;
    letter-spacing: 2px;
  }
  .message-panel { stroke: var(--gold); stroke-width: 2.5; }
  .message {
    font-family: 'Montserrat', sans-serif;
    font-weight: 300;
    font-size: 16.5px;
    fill: var(--white);
    text-anchor: middle;
  }
  .message-strong { font-weight: 600; font-size: 16.5px; }
  .message-lead { text-anchor: end; }
  .charity-name {
    font-family: 'Montserrat', sans-serif;
    font-weight: 700;
    font-size: 19px;
    fill: var(--deep-rose);
    text-anchor: middle;
  }
  .support-badge { fill: var(--ink); }
  .support-badge-label {
    font-family: 'Montserrat', sans-serif;
    font-weight: 700;
    font-size: 11px;
    fill: var(--white);
    text-anchor: middle;
  }
  .brand-ring { fill: none; stroke: var(--plum); stroke-width: 4; }
  .brand-name {
    font-family: 'Montserrat', sans-serif;
    font-weight: 700;
    font-size: 18px;
    fill: var(--plum);
    text-anchor: middle;
    letter-spacing: 1px;
  }
</style>
</head>
<body>
<svg class="insert-sheet" viewBox="0 0 1200 1200" xmlns="http://www.w3.org/2000/svg">
  <defs>
    <clipPath id="front-clip"><rect x="69" y="240" width="480" height="720"/></clipPath>
    <linearGradient id="panel-fill" x1="0" y1="0" x2="0" y2="1">
      <stop offset="0" stop-color="var(--panel-pink)"/>
      <stop offset="1" stop-color="var(--panel-pink-light)"/>
    </linearGradient>
    <radialGradient id="blossom-fill" cx="0.5" cy="0.5" r="0.5">
      <stop offset="0" stop-color="var(--blossom-light)"/>
      <stop offset="1" stop-color="var(--blossom-mid)" stop-opacity="0"/>
    </radialGradient>
  </defs>

  <!-- Front: thank you side -->
  <g class="front-side">
    <rect class="card-front" x="69" y="240" width="480" height="720"/>
    <g clip-path="url(#front-clip)">
      <circle class="faint-mark-ring" cx="494" cy="892" r="136"/>
      <text class="faint-mark-name" x="402" y="935">RIDGEWAY</text>
    </g>
    <g role="img" aria-label="Small flat illustration of people with laptops and speech bubbles sitting on the lettering">
      <rect x="282" y="488" width="40" height="44" rx="8" fill="#f7b2bf" opacity="0.55"/>
      <rect x="376" y="492" width="96" height="40" rx="8" fill="#f7b2bf" opacity="0.55"/>
      <rect x="256" y="618" width="40" height="20" rx="8" fill="#f7b2bf" opacity="0.45"/>
    </g>
    <text class="headline" x="122" y="606" font-size="103" textLength="370" lengthAdjust="spacingAndGlyphs">THANK</text>
    <line class="headline-rule" x1="144" y1="605" x2="490" y2="605"/>
    <text class="headline" x="177" y="710" font-size="103" textLength="228" lengthAdjust="spacingAndGlyphs">YOU</text>
    <line class="headline-rule" x1="186" y1="710" x2="412" y2="710"/>
  </g>

  <!-- Back: message side -->
  <g class="back-side">
    <rect class="card-back" x="654" y="240" width="480" height="720"/>
    <path class="message-panel" fill="url(#panel-fill)"
          d="M680,240 V590 Q680,748 894,748 Q1110,748 1110,590 V240"/>

    <text class="message" x="894" y="305">We would love to hear your feedback!</text>
    <text class="message" x="894" y="322">For every review we receive on our products,</text>
    <text class="message" x="894" y="339">we donate 100% of the proceeds of your order to</text>
    <text class="charity-name" x="894" y="367">TIDEWELL</text>
    <text class="message message-strong" x="894" y="392">a non profit organization dedicated</text>
    <text class="message message-strong" x="894" y="409">to preserving our oceans !</text>
    <text class="message" x="894" y="432">If you are not 100% satisfied</text>
    <text class="message" x="894" y="449">with your purchase or have any problems,</text>
    <text class="message" x="894" y="474">we will always resolve your issue.</text>
    <text class="message message-lead" x="938" y="491">please contact us via</text>
    <rect class="support-badge" x="945" y="477" width="50" height="18" rx="2"/>
    <text class="support-badge-label" x="970" y="490">Brisko</text>
    <text class="message" x="894" y="508">if you need assistance.</text>
    <text class="message" x="894" y="525">Insert needs to be well organized and information</text>
    <text class="message" x="894" y="542">presented in a clear and visually appealing way.</text>

    <g role="img" aria-label="Pale pink blossom branch decorating the left side of the panel">
      <rect x="654" y="600" width="190" height="180" rx="80" fill="url(#blossom-fill)"/>
    </g>
    <g role="img" aria-label="Pale pink blossom branch decorating the right side of the panel">
      <rect x="944" y="600" width="190" height="180" rx="80" fill="url(#blossom-fill)"/>
    </g>

    <circle class="brand-ring" cx="894" cy="852" r="72"/>
    <text class="brand-name" x="894" y="878" textLength="110" lengthAdjust="spacingAndGlyphs">RIDGEWAY</text>
  </g>
</svg>
</body>
</html>
```